Book Cover (HALF OF ALL WORRIES FADE AWAY)

This book is a series of blog posts from my blog, Notes Fit for Borrowing, which is at glenmarwick.com/blog.
The book is to be called:
HALF OF ALL WORRIES FADE AWAY
And 51 other Notes Fit for Borrowing from the Small Business Sage
(Notes Fit for Borrowing) should be italicized.
My name is Glen Marwick, M.B.A.

I will need three variations for my paperback, hardcover and e-book.
Here are some of the blog titles and their topics:
Preparing Your Small Business For Recession small business recession
Should I Incorporate My Business? Should I Incorporate My Business?
Alternative to Minority Shareholder In Small Private Companies minority shareholder
Small Business Culture – Getting it Right Small Business Culture
What is The Right Way to Fire Someone The Right Way to Fire Someone
The Five Basic Leadership Principles Leadership Principles
10 Tips for New Entrepreneurs – Sure Ways to Increase Your Chances of Success
10 things to consider before becoming an entrepreneur
Strategy vs Biz Plans small business strategy
Closing Sales close the sale
Breakeven break even
Growth makes cash flow suck cash flow issues
Think Twice About Offering Early Payment Discounts prepayment discounts
Firing Customers firing customers
Collections best practices getting paid faster
The Cash Flow Statement cash flow statement
Using Paralegals paralegal
Radical Candor radical candor
Why No is the Second Best Word to a Salesperson's ears value of no
The $8 Million Problem -
Contractor vs Employee contractor vs employee
The Vantrell sales tactic
Systems Turn Goals From Dreams Into Reality Systems vs Goals
The Importance of Realistic Goals stretch goals
Why The Owner Must Review Every Hire hiring for values
Systems Thinking for Small Biz: The Case for SOPs systems thinking
Trust Your Gut business intuition
Grease and friction grease vs friction
Left alone, 90% of problems solve themselves strategic inaction
Referrals Are Great—But Not a Growth Strategy referrals
The Lean Marketing Machine: 7 Hacks to Grow Your Small Business Fast marketing hacks
The Small Business Health Check small business health check
How to Spot a Customer Headed for Trouble — Before They Take You Down With Them customer warning signs
We Are What We Repeatedly Do habits
The Smartest People Know When to Play Dumb playing dumb
Before You Scale, Do the Math unit economics
AI for Small Business: Practical Tools and Use Cases AI for Small Business
Title: Tell Me Right Now—Why Can’t We Raise Your Prices? small business pricing
Why Your Real Competitor Isn’t Who You Think creative destruction
Good Enough Might Be Great satisficing
Bootstrapping: Building Your Business on Your Terms bootstrapping
Building Resilient Companies That Never Have to Bet the Farm bet the farm
We Always Overshoot: From Fiber to Cannabis to AI AI overbuild
A Bias Toward Action bias toward ation
Choosing the Right Business Owner Title business owner title
Jobs to Be Done: Understanding What Your Customers Really Want Jobs to Be Done
Forget Money. Here’s What Really Motivates People. motivation

Target Market(s)

Small business operators, business school students

Industry/Entity Type

Small business

Colors

Designer to choose colors to be used in the design.

Requirements
Should not have
• Should not look cartoonish

```html
<!DOCTYPE html>
<html lang="en">
<head>
<meta charset="utf-8">
<title>Half of All Worries Fade Away — Book Cover</title>
<link rel="stylesheet" href="https://fonts.googleapis.com/css2?family=Bebas+Neue&family=Montserrat:wght@500&family=Mulish:ital,wght@1,400&display=swap">
<style>
  :root {
    --cover-bg: #b8ced5;
    --title-blue: #1b56a6;
    --title-navy: #0c2448;
    --subtitle-ink: #0f2545;
    --band-dark: #123a74;
    --band-mid: #1b4f98;
    --author-ink: #c3d6de;
    --rope-tan: #d7bf9c;
    --rope-shadow: #a9c3cc;
  }
  * { margin: 0; padding: 0; box-sizing: border-box; }
  html, body { width: 873px; height: 1200px; overflow: hidden; background: var(--cover-bg); }

  .cover {
    position: relative;
    width: 873px;
    height: 1200px;
    background: var(--cover-bg);
  }

  .title {
    position: absolute;
    left: 0;
    top: 128px;
    width: 100%;
    text-align: center;
    font-family: "Bebas Neue", "Arial Narrow", sans-serif;
    font-weight: 400;
  }
  .title-line {
    display: block;
    line-height: 1;
    background: linear-gradient(to bottom, var(--title-blue) 0%, var(--title-navy) 45%, var(--title-navy) 60%, var(--title-blue) 100%);
    -webkit-background-clip: text;
    background-clip: text;
    color: transparent;
    -webkit-text-fill-color: transparent;
  }
  .title-line--wide {
    font-size: 150px;
    height: 150px;
    letter-spacing: 2px;
    transform: scaleX(1.22);
  }
  .title-line--tall {
    font-size: 226px;
    height: 188px;
    line-height: 0.9;
    letter-spacing: 1px;
  }
  .title-line--wide + .title-line--tall { margin-top: 4px; }
  .title-line--tall + .title-line--wide { margin-top: 14px; }
  .title-line--last { font-size: 184px; height: 160px; line-height: 0.95; margin-top: 12px; }

  .subtitle {
    position: absolute;
    left: 0;
    top: 792px;
    width: 100%;
    text-align: center;
    font-family: "Mulish", "Avenir Next", sans-serif;
    font-style: italic;
    font-weight: 400;
    font-size: 35px;
    line-height: 39px;
    letter-spacing: 0.5px;
    color: var(--subtitle-ink);
  }

  .cover-art {
    position: absolute;
    left: 160px;
    top: 905px;
    width: 560px;
    height: 175px;
    border-radius: 90px;
    background: radial-gradient(ellipse at 50% 50%, var(--rope-tan) 0%, rgba(215,191,156,0.55) 40%, var(--rope-shadow) 75%, var(--cover-bg) 100%);
  }

  .author-band {
    position: absolute;
    left: 0;
    bottom: 0;
    width: 100%;
    height: 88px;
    display: flex;
    align-items: center;
    justify-content: center;
    background: linear-gradient(to right, var(--band-dark) 0%, var(--band-mid) 50%, var(--band-dark) 100%);
  }
  .author-name {
    font-family: "Montserrat", "Helvetica", sans-serif;
    font-weight: 500;
    font-size: 36px;
    letter-spacing: 1px;
    color: var(--author-ink);
  }
</style>
</head>
<body>
  <main class="cover">
    <h1 class="title">
      <span class="title-line title-line--wide">Half of All</span>
      <span class="title-line title-line--tall">Worries</span>
      <span class="title-line title-line--wide">Fade</span>
      <span class="title-line title-line--tall title-line--last">Away</span>
    </h1>

    <p class="subtitle">And 51 other <em>Notes Fit for Borrowing</em><br>from the Small Business Sage</p>

    <div class="cover-art" role="img" aria-label="Photograph of a neatly coiled rope whose loose end runs into a tangled knot"></div>

    <footer class="author-band">
      <span class="author-name">GLEN MARWICK, M.B.A</span>
    </footer>
  </main>
</body>
</html>
```